Editorial / Brochure Designer – Adobe InDesign Luxury Travel Publication Redesign

CREATIVE BRIEF
Editorial / Brochure Designer – Adobe InDesign
Luxury Travel Publication Redesign

Project:
Company brochure redesign — Wandering Horizons for Harbor Lanterns. Premium, full-color print publication.

Current State:
106-page brochure built on a stock design template. While the content foundation is strong, the design and layout repeat the same formula across all seven major sections.

Target Length:
Approximately 75–85 pages after planned content edits and consolidation. We are open to the designer's recommendations once the revised copy is reviewed and flowed into the new design.

Format:
8.5" × 11" portrait finished pages with 11" × 17" facing-page spreads. Full-color professional print production. Final binding is TBD, likely perfect/PUR perfect binding.

Audience:
Existing referral clients, including clients we would like to re-engage, as well as new referrals. Our clients are loyal, often multigenerational, higher-end travelers planning meaningful vacations, celebrations, and bucket-list journeys.

Primary Goal:
Create an evergreen "keep and refer back to" publication—not a seasonal mailer. The brochure should avoid dates, "new in 2027" messaging, or other content that will quickly expire.

Brand Feel:
Personal, relationship-driven, sophisticated, inspiring and "different and outside the box." It should not feel like a generic luxury travel agency brochure or stock/template design.

Think premium travel magazine / coffee-table publication rather than a traditional travel catalog.

Must Avoid:
Template monotony. The existing brochure relies heavily on the same layout skeleton:

Section divider → headline → pitch → bullet list → repeat

The redesigned publication must introduce variety in pacing, layout, photography, typography, white space, and visual rhythm from section to section, while still feeling cohesive and unmistakably Harbor Lanterns.

The Design Challenge
This is not simply a cleanup or reformatting project.

The selected designer will receive the existing 106-page brochure as the content foundation, along with revised/trimmed copy, brand assets, photography, and detailed editorial recommendations.

We want you to approach the publication with fresh eyes and a new creative perspective.

Some pages may need to become dramatic two-page spreads. Others may need to be minimal and quiet. Some information may work better as an editorial feature, comparison, sidebar, testimonial, pull quote, or visual story.

We want a designer who understands editorial pacing across a long publication, rather than simply creating an attractive template and repeating it.

Planned Content Changes/Priorities
The revised publication will include changes such as:

• Eliminating repetitive pages and messaging
• Creating one strong "Why Harbor Lanterns" narrative
• Adding a personal "Meet Rosa" / founder story
• A personal "Meet Rosa" spread near the front — photo, founder story, why referrals are the only marketing you've ever needed
• A short "how we've grown" page/timeline showing the range of travel you now cover
• Introducing recurring "Rosa's Pick" editorial callouts
• Incorporating authentic client stories/testimonials per major section
• Removing or relocating time-sensitive content
• Section openers that feel distinct from each other in layout, not just in photo subject
• Strengthening the final call to action
• Bringing more personality and Harbor Lanterns-specific storytelling into the publication

We specifically want someone with demonstrated experience designing:

• 50–150+ page publications
• Magazines
• Luxury brochures
• Product catalogs
• Lookbooks
• High-end print collateral
• Professional print publications

Experience with luxury travel, hospitality, lifestyle, cruise, resort, or premium consumer brands is highly desirable.

Advanced Adobe InDesign expertise is required, including Parent/Master Pages, paragraph and character styles, grids, long-document workflows, typography, image management, preflight, CMYK, bleeds, packaging, and professional print-ready PDF production.

We want to evaluate your:
• Creative direction
• Editorial judgment
• Typography
• Photography treatment
• Visual hierarchy
• Use of white space
• Page-to-page pacing
• Ability to elevate our existing brand

The successful designer will then be considered for the complete 75–85+ page publication redesign.

To Apply
Please provide:

• 2–4 examples of long-form publications you personally designed, preferably 50+ pages.
• Your experience with professional print production.
• Confirmation that you work in Adobe InDesign and can provide packaged source files so that we can edit at a later date.

Please prioritize relevant editorial work. We are specifically looking for long-form publication design experience, rather than portfolios focused primarily on logos, social media, websites, Canva templates, single-page flyers, or short brochures.

```html
<!DOCTYPE html>
<html lang="en">
<head>
<meta charset="utf-8">
<title>Wandering Horizons – Harbor Lanterns Brochure Pages</title>
<link href="https://fonts.googleapis.com/css2?family=Barlow:wght@400;500;600;700;800&family=Great+Vibes&family=Allura&display=swap" rel="stylesheet">
<style>
:root{
  --board:#808080;
  --paper:#ffffff;
  --navy:#1f3f7f;
  --navy-deep:#1a3570;
  --ink:#1c1c1c;
  --body:#444a55;
  --coral:#e0552f;
  --sky:#4fb6e6;
  --rule:#c9ccd2;
}
*{margin:0;padding:0;box-sizing:border-box}
html,body{width:1200px;height:957px;overflow:hidden;background:var(--board)}
body{position:relative;font-family:"Barlow",Arial,sans-serif;color:var(--ink)}
.page{position:absolute;width:300px;height:388px;background:var(--paper);overflow:hidden}
.photo{position:absolute}
.url{position:absolute;left:22px;top:22px;font-size:5.6px;color:var(--navy)}
.footer-band{position:absolute;top:367px;height:21px;background:var(--navy);color:#fff;font-size:5.4px;display:flex;align-items:center;white-space:nowrap}
.folio{position:absolute;top:375px;font-size:5.4px;color:#777}
.body-copy{font-size:5.5px;line-height:7px;color:var(--body)}
.body-copy p{margin-bottom:7px}
.script{font-family:"Great Vibes","Allura",cursive;font-weight:400}
.coral-rule{position:absolute;height:1.2px;width:34px;background:var(--coral)}

/* wordmark: plain set name, one colour, one weight */
.wordmark{position:absolute;font-family:"Barlow",Arial,sans-serif;font-weight:500;color:var(--navy);white-space:nowrap}

/* cover */
.cover{left:104px;top:70px}
.cover-photo{inset:0;background:linear-gradient(180deg,#8fb8dc 0%,#c9d9e6 14%,#c46a4a 26%,#3d5a4e 40%,#1f6f86 55%,#2a8cc0 72%,#1d6ea8 100%)}
.cover .wordmark{top:50px;left:0;right:0;text-align:center;font-size:18px;letter-spacing:.3px}
.cover-title{position:absolute;left:0;right:0;top:262px;text-align:center;color:#fff}
.cover-title .script{font-size:40px;line-height:32px;display:block;margin-left:14px}
.cover-title .bold{font-size:40px;font-weight:800;line-height:40px;color:#dff3ff;letter-spacing:-.5px;display:block}
.cover-title .sub{font-size:15px;line-height:18px;font-weight:400;display:block;margin-left:-30px}

/* spread 1 left */
.intro{left:492px;top:70px}
.intro h2{position:absolute;left:22px;top:52px;font-size:9px;font-weight:600}
.intro .tag{position:absolute;left:22px;top:64px;font-size:12px;color:var(--navy)}
.intro .body-copy{position:absolute;left:22px;top:106px;width:125px}

/* spread 1 right */
.why{left:797px;top:70px}
.why-hero{left:0;top:0;width:300px;height:96px;background:linear-gradient(180deg,#e9a54a 0%,#f4d18a 20%,#6f9fa8 42%,#cfe1e4 70%,#ffffff 100%)}
.why .url{color:#fff}
.why h2{position:absolute;left:22px;top:60px;font-size:12.5px;font-weight:400;color:var(--ink)}
.why h2 strong{font-weight:700;color:var(--navy)}
.feature{position:absolute;width:82px}
.feature svg{display:block;width:13px;height:13px;margin-bottom:6px}
.feature h3{font-size:6.3px;line-height:8px;font-weight:500;color:var(--ink);margin-bottom:7px}
.feature p{font-size:5.2px;line-height:7px;color:var(--body)}
.feature-rule{position:absolute;height:.6px;width:62px;background:var(--rule)}
.specialist{position:absolute;left:201px;top:96px;width:99px;height:246px;background:var(--navy);color:#fff;text-align:center;padding-top:23px}
.specialist .lead{font-size:7px;line-height:9px}
.specialist .big{font-size:9px;font-weight:600;line-height:11px}
.specialist .script{font-size:18px;color:var(--coral);line-height:16px;display:block;margin-bottom:8px}
.specialist ul{list-style:none}
.specialist li{font-size:4.4px;line-height:5.6px;margin:0 auto;width:70px;margin-bottom:9px}
.specialist li::before{content:"";display:block;width:5px;height:5px;border-radius:50%;background:#fff;margin:0 auto 6px}

/* toc */
.toc{left:104px;top:499px}
.toc-photo{left:0;top:0;width:88px;height:388px;background:linear-gradient(180deg,#c6dbe8 0%,#6e8ea3 20%,#3e6a5e 45%,#557f3a 70%,#2f5a32 100%)}
.toc h2{position:absolute;left:115px;top:53px;font-size:11.5px;font-weight:700;color:var(--navy)}
.toc-list{position:absolute;left:115px;top:97px;width:160px;list-style:none}
.toc-list li{height:21.2px;font-size:5.4px;line-height:6.8px}
.toc-list .row{display:flex;font-weight:600}
.toc-list .num{width:10px}
.toc-list .dots{flex:1;border-bottom:.6px dotted var(--ink);margin:0 1px 1.6px}
.toc-list .desc{padding-left:10px;color:var(--body)}
.toc .wordmark{top:334px;left:115px;font-size:11px}

/* bottom spread */
.harbor{left:492px;top:499px}
.harbor-photo{inset:0;background:linear-gradient(180deg,#2f6fc0 0%,#5b94d4 18%,#2d5a33 40%,#3f6a3a 55%,#7a5a4a 68%,#243a3c 82%,#1b2b2a 100%)}
.harbor .url{color:#9aa9c8}
.alaska{left:797px;top:499px}
.alaska .title{position:absolute;left:20px;top:42px;font-size:34px;color:var(--navy);line-height:36px}
.alaska .divider{position:absolute;left:135px;top:53px;width:.8px;height:20px;background:#999}
.alaska .tagline{position:absolute;left:151px;top:57px;font-size:7.2px;line-height:9.5px;font-weight:500}
.alaska-photo{left:22px;top:105px;width:128px;height:140px;background:linear-gradient(180deg,#8fb1d6 0%,#d8e2ea 30%,#7d8a7a 55%,#5e7a3a 80%,#6d7a34 100%)}
.alaska-circle{left:50px;top:210px;width:70px;height:70px;border-radius:50%;border:2px solid var(--navy);background:radial-gradient(circle at 50% 40%,#e8b060 0%,#c58a4a 50%,#6a88a8 100%)}
.alaska .body-copy{position:absolute;left:173px;top:105px;width:105px}
.alaska .body-copy p{margin-bottom:6.5px}
.works{position:absolute;left:173px;top:231px;width:112px}
.works h4{font-size:6.2px;font-weight:600;margin-bottom:6px}
.works ul{list-style:none}
.works li{font-size:5.4px;line-height:6.8px;color:var(--body);display:flex;gap:5px;margin-bottom:3px}
.works li::before{content:"";flex:0 0 4.5px;height:4.5px;border-radius:50%;background:var(--navy);margin-top:1px}
.lines-head{position:absolute;left:22px;top:295px;font-size:6.3px;font-weight:700;color:var(--navy)}
.lines-rule{position:absolute;left:22px;top:304px;width:256px;height:.6px;background:var(--rule)}
.line-card{position:absolute;top:313px;width:80px}
.line-card .script{font-family:"Allura",cursive;font-size:8px;color:var(--coral);display:block;margin-bottom:2px}
.line-card p{font-size:5.3px;line-height:6.8px;color:var(--body)}
</style>
</head>
<body>

<!-- Cover -->
<section class="page cover">
  <div class="photo cover-photo" role="img" aria-label="Mountain lake at sunrise with red peaks reflected in turquoise water"></div>
  <div class="wordmark">Harbor Lanterns</div>
  <div class="cover-title">
    <span class="script">Wandering</span>
    <span class="bold">Horizons</span>
    <span class="sub">One Trusted Concierge</span>
  </div>
</section>

<!-- Intro page -->
<section class="page intro">
  <div class="url">www.Harborlanterns.Com</div>
  <h2>We Don’t Just Plan Vacations.</h2>
  <div class="tag script">We Create Memories That Last</div>
  <div class="coral-rule" style="left:22px;top:82px"></div>
  <div class="body-copy">
    <p>For nearly 30 years, Harbor Lanterns has helped travelers explore the world with confidence, personalized service, and unforgettable experiences.</p>
    <p>Whether you’re celebrating a milestone, bringing generations together, rewarding your team, or finally taking the bucket-list vacation you’ve always imagined, our mission remains the same:</p>
    <p>To make every journey effortless, meaningful, and unforgettable.</p>
    <p>From your first conversation until you return home, our team is by your side—offering expert guidance, managing every detail, and providing peace of mind before, during, and after your travels.</p>
    <p>Because extraordinary vacations don’t happen by chance.</p>
    <p>They happen through experience.</p>
  </div>
  <div class="photo" style="left:171px;top:0;width:129px;height:342px;background:linear-gradient(180deg,#3b5f8c 0%,#e59a3e 20%,#6b6a70 38%,#2c3b56 55%,#e8e6e2 75%,#b9a79a 100%)" role="img" aria-label="Whitewashed clifftop village with a blue-domed chapel above the sea at sunset"></div>
  <div class="folio" style="left:12px">01</div>
  <div class="footer-band" style="left:22px;right:0;padding-left:25px">Harbor Lanterns&nbsp; | &nbsp;Toll-free 1-800-555-0142&nbsp; | &nbsp;Local 555-555-0188&nbsp; | &nbsp;rosa@harborlanterns.com</div>
</section>

<!-- Why page -->
<section class="page why">
  <div class="photo why-hero" role="img" aria-label="Golden sunrise over ocean waves"></div>
  <div class="url">www.Harborlanterns.Com</div>
  <h2>Why Travelers Choose <strong>HARBOR LANTERNS</strong></h2>
  <div class="coral-rule" style="left:22px;top:82px"></div>

  <div class="feature" style="left:22px;top:102px">
    <svg viewBox="0 0 20 20" fill="none" stroke="var(--navy)" stroke-width="1.6"><path d="M6 3h8v5a4 4 0 0 1-8 0z"/><path d="M10 12v3M6.5 17h7"/></svg>
    <h3>Nearly 30 Years<br>of Expertise</h3>
    <p>Trusted travel advisors creating unforgettable journeys since 1997.</p>
  </div>
  <div class="feature" style="left:106px;top:102px">
    <svg viewBox="0 0 20 20" fill="none" stroke="var(--navy)" stroke-width="1.6"><circle cx="10" cy="10" r="8"/><path d="M13 7l-2 4-4 2 2-4z"/></svg>
    <h3>Personalized<br>Vacation design</h3>
    <p>Every itinerary is thoughtfully tailored to your travel style, interests, budget, and goals.</p>
  </div>
  <div class="feature-rule" style="left:22px;top:169px"></div>
  <div class="feature-rule" style="left:106px;top:169px"></div>

  <div class="feature" style="left:22px;top:176px">
    <svg viewBox="0 0 20 20" fill="var(--navy)"><path d="M3 15a7 7 0 0 1 14 0z"/><rect x="1" y="15.5" width="18" height="2"/><circle cx="10" cy="6" r="1.3"/></svg>
    <h3>Concierge-level<br>Service</h3>
    <p>From planning and documentation to dining reservations and special requests—we manage every detail.</p>
  </div>
  <div class="feature" style="left:106px;top:176px">
    <svg viewBox="0 0 20 20" fill="none" stroke="var(--navy)" stroke-width="1.5"><path d="M1 8l4-3 5 3 5-3 4 3M4 10l5 5 2-1 5-5M8 9l3 3"/></svg>
    <h3>Global Preferred<br>Partnerships</h3>
    <p>Exclusive relationships with the world’s leading cruise lines, resorts, tour operators, and luxury travel brands.</p>
  </div>
  <div class="feature-rule" style="left:22px;top:260px"></div>
  <div class="feature-rule" style="left:106px;top:260px"></div>

  <div class="feature" style="left:22px;top:267px">
    <svg viewBox="0 0 20 20" fill="none" stroke="var(--navy)" stroke-width="1.6"><path d="M3 12V9a7 7 0 0 1 14 0v3"/><rect x="2" y="11" width="3" height="5" rx="1" fill="var(--navy)"/><rect x="15" y="11" width="3" height="5" rx="1" fill="var(--navy)"/></svg>
    <h3>Here When You<br>Need Us</h3>
    <p>Personal support before, during, and after your journey.</p>
  </div>
  <div class="feature" style="left:106px;top:267px">
    <svg viewBox="0 0 20 20" fill="none" stroke="var(--navy)" stroke-width="1.6"><path d="M6 3h8v5a4 4 0 0 1-8 0z"/><path d="M10 12v3M6.5 17h7"/></svg>
    <h3>Passionate<br>About Travel</h3>
    <p>We love what we do and it shows in every vacation we plan and every relationship we build.</p>
  </div>

  <div class="specialist">
    <div class="lead">Specialists in</div>
    <div class="big">Extraordinary</div>
    <span class="script">Travel</span>
    <ul>
      <li>Luxury Ocean and River Cruises</li>
      <li>Alaska and Expedition Travel</li>
      <li>Luxury Resorts</li>
      <li>Multigenerational Vacations</li>
      <li>Groups and Incentive Travel</li>
      <li>Private and Hosted Journeys</li>
    </ul>
  </div>
  <div class="footer-band" style="left:0;width:278px;padding-left:22px">Harbor Lanterns&nbsp; | &nbsp;Toll-free 1-800-555-0142&nbsp; | &nbsp;Local 555-555-0188&nbsp; | &nbsp;rosa@harborlanterns.com</div>
  <div class="folio" style="left:283px">02</div>
</section>

<!-- Table of contents -->
<section class="page toc">
  <div class="photo toc-photo" role="img" aria-label="Fjord valley with snowy peaks above a green farmstead"></div>
  <h2>TABLE OF CONTENTS</h2>
  <div class="coral-rule" style="left:115px;top:71px"></div>
  <ol class="toc-list">
    <li><div class="row"><span class="num">1.</span>Why Harbor Lanterns<span class="dots"></span>3-4</div><div class="desc">How we help you plan the trip that matters</div></li>
    <li><div class="row"><span class="num">2.</span>Legacy Travel<span class="dots"></span>5-13</div><div class="desc">Multigenerational family journeys</div></li>
    <li><div class="row"><span class="num">3.</span>River Cruising<span class="dots"></span>15-32</div><div class="desc">Every river tells a story</div></li>
    <li><div class="row"><span class="num">4.</span>Alaska Travel<span class="dots"></span>33-42</div><div class="desc">Glaciers, wildlife, and wild coastline</div></li>
    <li><div class="row"><span class="num">5.</span>Expedition Travel<span class="dots"></span>43-56</div><div class="desc">Antarctica, the Galapagos, and beyond</div></li>
    <li><div class="row"><span class="num">6.</span>Ocean Cruise Voyages<span class="dots"></span>57-70</div><div class="desc">Iconic ships, endless amenities</div></li>
    <li><div class="row"><span class="num">7.</span>All-Inclusive Travel<span class="dots"></span>71-86</div><div class="desc">Everything taken care of</div></li>
    <li style="height:28px"><div class="row"><span class="num">8.</span>Incentive Travel<span class="dots"></span>87-102</div><div class="desc">Extraordinary results deserve extraordinary<br>experiences</div></li>
    <li><div class="row"><span class="num">9.</span>Ready to Start Planning?<span class="dots"></span>103-104</div><div class="desc">Next steps and contact information</div></li>
  </ol>
  <div class="wordmark">Harbor Lanterns</div>
</section>

<!-- Harbor photo page -->
<section class="page harbor">
  <div class="photo harbor-photo" role="img" aria-label="Colorful wooden houses on stilts along a creek boardwalk beneath evergreen forest"></div>
  <div class="url">www.Harborlanterns.Com</div>
  <div class="folio" style="left:12px;color:#9aa9c8">03</div>
  <div class="footer-band" style="left:22px;right:0;padding-left:25px">Harbor Lanterns&nbsp; | &nbsp;Toll-free 1-800-555-0142&nbsp; | &nbsp;Local 555-555-0188&nbsp; | &nbsp;rosa@harborlanterns.com</div>
</section>

<!-- Alaska page -->
<section class="page alaska">
  <div class="url">www.Harborlanterns.Com</div>
  <div class="title script">Alaska</div>
  <div class="divider"></div>
  <div class="tagline">Where Wonder Is Shared—<br>and Remembered for a Lifetime</div>
  <div class="coral-rule" style="left:22px;top:82px"></div>
  <div class="photo alaska-photo" role="img" aria-label="Family hiking toward snowy mountains and a glacier valley"></div>
  <div class="photo alaska-circle" role="img" aria-label="Family portrait in warm jackets outdoors"></div>
  <div class="body-copy">
    <p>An Alaska cruise offers a breathtaking backdrop for family connection.</p>
    <p>Towering glaciers, wildlife encounters, and awe-inspiring landscapes create unforgettable shared experiences.</p>
    <p>Watch whales surface together.</p>
    <p>Stand in silence as glaciers thunder into the sea.</p>
    <p>Explore charming frontier towns rich with history.</p>
  </div>
  <div class="works">
    <h4>Why It Works for Families:</h4>
    <ul>
      <li>Educational and inspiring for all ages</li>
      <li>Comfortable, easy travel with minimal logistics</li>
      <li>Shared “wow” moments every day</li>
    </ul>
  </div>
  <div class="lines-head">FEATURED CRUISE LINES:</div>
  <div class="lines-rule"></div>
  <div class="line-card" style="left:22px"><span class="script">Coral Crest Cruises –</span><p>Ideal for active families with diverse onboard experiences</p></div>
  <div class="line-card" style="left:139px"><span class="script">Silver Meridian Cruises –</span><p>Elevated comfort, refined dining, and immersive excursions</p></div>
  <div class="footer-band" style="left:0;width:278px;padding-left:22px">Harbor Lanterns&nbsp; | &nbsp;Toll-free 1-800-555-0142&nbsp; | &nbsp;Local 555-555-0188&nbsp; | &nbsp;rosa@harborlanterns.com</div>
  <div class="folio" style="left:283px">04</div>
</section>

</body>
</html>
```